Business Card Ayurvedic Massage

I'm starting with my ayurvedic massage business and need a business card design. The design should be inline with my brand/logo as well as with the design of my website (www.lumo-thara.ch).
Front: logo and text "Ayurvedische Massagen"
back: name and adress (see details https://www.lumo-thara.ch/kontakt.html)

```html
<!DOCTYPE html>
<html lang="de">
<head>
<meta charset="utf-8">
<title>lumo-thara – Visitenkarte</title>
<link href="https://fonts.googleapis.com/css2?family=Lato:wght@400&family=Tinos:wght@400&display=swap" rel="stylesheet">
<style>
  :root{
    --stage:#2a2a2a;
    --card-red:#8d1219;
    --card-red-light:#a01c22;
    --card-red-dark:#6e0c12;
    --gold:#e3ad3a;
    --gold-soft:#d9a441;
    --cream:#f4e6cf;
  }
  *{margin:0;padding:0;box-sizing:border-box}
  html,body{width:1200px;height:1200px;overflow:hidden}
  body{background:var(--stage);position:relative}
  .card{
    position:absolute;left:185px;width:830px;
    background:radial-gradient(ellipse at 50% 45%,var(--card-red-light) 0%,var(--card-red) 55%,var(--card-red-dark) 100%);
    box-shadow:0 8px 18px rgba(0,0,0,.55);
  }
  .card--front{top:90px;height:476px}
  .card--back{top:640px;height:470px;text-align:center;font-family:'Lato',sans-serif;color:var(--gold)}

  .brand{position:absolute;top:26px;left:0;right:0;text-align:center}
  .brand__name{
    display:inline-flex;align-items:center;gap:8px;
    font-family:'Tinos',serif;font-size:22px;color:var(--gold);letter-spacing:.5px
  }
  .brand__dot{width:10px;height:10px;border-radius:50%;background:var(--gold)}
  .brand__tagline{
    margin-top:14px;font-family:'Tinos',serif;font-size:8.5px;
    color:var(--cream);letter-spacing:.3px
  }

  .menu-photo{position:absolute;top:115px;width:113px;height:304px}
  .photo--lamp{left:20px;background:linear-gradient(180deg,#3a1a08,#b7761e 55%,#f0c56a)}
  .photo--treatment{left:188px;background:linear-gradient(180deg,#3b2416,#8a4a22 50%,#c58a3c)}
  .photo--candles{left:354px;background:radial-gradient(circle at 70% 45%,#e0521e,#a5200e 55%,#5a0c08)}
  .photo--portrait{left:524px;background:linear-gradient(180deg,#7a4a30,#d8c2a0 50%,#ecdcc0)}
  .photo--arches{left:694px;background:radial-gradient(circle at 55% 55%,#ffd36a,#b5621e 35%,#4a2510 80%)}

  .menu-label{
    position:absolute;top:446px;width:140px;margin-left:-70px;text-align:center;
    font-family:'Tinos',serif;font-size:16px;color:var(--cream)
  }

  .back__title{position:absolute;top:113px;left:0;right:0;font-size:43px;line-height:1}
  .back__address{position:absolute;top:192px;left:0;right:0;font-size:23px;line-height:33px}
  .back__contact{position:absolute;top:276px;left:0;right:0;font-size:23px;line-height:33px}
</style>
</head>
<body>

<section class="card card--front">
  <header class="brand">
    <div class="brand__name"><span class="brand__dot"></span>lumo-thara</div>
    <div class="brand__tagline">AYURVEDISCHE MASSAGEN</div>
  </header>

  <div class="menu-photo photo--lamp" role="img" aria-label="Messing-Öllampe mit Flamme und Blütenblättern"></div>
  <div class="menu-photo photo--treatment" role="img" aria-label="Ayurvedische Kräuterstempel und Ölschalen"></div>
  <div class="menu-photo photo--candles" role="img" aria-label="Kreis aus brennenden Öllichtern"></div>
  <div class="menu-photo photo--portrait" role="img" aria-label="Frau in festlichem indischem Gewand mit Schmuck"></div>
  <div class="menu-photo photo--arches" role="img" aria-label="Säulengang mit Bögen im warmen Gegenlicht"></div>

  <span class="menu-label" style="left:76px">Ayurveda</span>
  <span class="menu-label" style="left:244px">Behandlungen</span>
  <span class="menu-label" style="left:411px">Preise</span>
  <span class="menu-label" style="left:580px">Portrait</span>
  <span class="menu-label" style="left:750px">Kontakt</span>
</section>

<section class="card card--back">
  <h1 class="back__title" style="font-weight:400">Bitte keine Werbung</h1>
  <p class="back__address">Mira Feldmann, lumo-thara<br>Lindenweg 14, 8855 Wangen (SZ)</p>
  <p class="back__contact">+41 79 555 01 23<br>info@lumo-thara.ch<br>www.lumo-thara.ch</p>
</section>

</body>
</html>
```